NEED A BUSINESS CARD FOR A NEW ELECTRICAL BUSINESS

HI I am after a new business card for my new electrical business I have a logo that I have attached its the one in blue, I would like that on the front and on the back my name- Marcus fell, Email marcusfell@tralvinet.com, mobile 0491570156, licence no# vic 48107, nsw 315042k I wont something that is a stand out from the rest but at the same time is neat as being a new business I wont it to catch peoples eye on the front of the card I would like the logo and not much else.
And on the back as well I would like a slogan saying something like
Quality-Reliable-Service

Hi all on the back of the card I would like a little slogan like Quality-Reliable-Service something like that would be good thanks

Hi all the business card needs to have both these licence numbers on it                                                  VIC-48107 nsw-315042k

```html
<!DOCTYPE html>
<html lang="en">
<head>
<meta charset="utf-8">
<title>Fellway Electrical – Business Card Concepts</title>
<link rel="stylesheet" href="https://fonts.googleapis.com/css2?family=Exo+2:wght@400;600;800&family=Open+Sans:wght@400;600;700&family=Playfair+Display:wght@700&family=Michroma&display=swap">
<style>
  :root {
    --stage-1: #3b3531;
    --stage-2: #4a413a;
    --stage-3: #3d3d3d;
    --ink: #101010;
    --charcoal: #2a2a2a;
    --charcoal-deep: #1b1b1b;
    --white: #ffffff;
    --blue: #1f6fc6;
    --blue-deep: #1450a0;
    --orange: #f28a1c;
    --orange-logo: #e2621a;
    --green: #5fd13a;
    --green-deep: #2f9e2a;
    --grey-text: #bdbdbd;
  }
  * { box-sizing: border-box; margin: 0; padding: 0; }
  html, body { width: 1200px; height: 2404px; overflow: hidden; background: #2e2e2e; }
  body { font-family: "Open Sans", Arial, sans-serif; }

  .concept { position: relative; width: 1200px; height: 801px; overflow: hidden; }
  .concept--blue { background: var(--stage-1); }
  .concept--orange { background: var(--stage-2); }
  .concept--green { background: var(--stage-3); height: 802px; }

  .card {
    position: absolute; width: 620px; height: 354px; overflow: hidden;
    border-radius: 4px; box-shadow: 0 14px 30px rgba(0,0,0,.45);
  }
  .card--front { left: 150px; top: 40px; }
  .card--back { left: 430px; top: 410px; }

  .brand-mark { font-family: "Exo 2", sans-serif; font-weight: 800; line-height: 1; letter-spacing: 2px; white-space: nowrap; }
  .brand-caption { font-family: "Exo 2", sans-serif; font-weight: 400; font-size: 11px; letter-spacing: 1px; white-space: nowrap; }
  .slogan { font-family: "Exo 2", sans-serif; font-weight: 400; letter-spacing: 3px; white-space: nowrap; }

  /* ---------- Blue concept ---------- */
  .blue-front { background: linear-gradient(160deg, #2b2b2b 0%, #111 60%, #080808 100%); }
  .blue-front .brand-mark { position: absolute; left: 120px; top: 70px; font-size: 92px; color: var(--blue); }
  .blue-front .brand-caption { position: absolute; left: 124px; top: 170px; color: var(--grey-text); }
  .blue-front .slogan { position: absolute; left: 124px; top: 192px; font-size: 22px; color: var(--white); }

  .blue-back { background: var(--white); }
  .blue-back .top-band { position: absolute; left: 0; top: 0; width: 100%; height: 132px; background: linear-gradient(160deg, #2a2a2a, #0c0c0c); }
  .blue-back .brand-mark { position: absolute; left: 40px; top: 30px; font-size: 50px; color: var(--blue); }
  .blue-back .brand-caption { position: absolute; left: 42px; top: 86px; color: var(--grey-text); font-size: 9px; }
  .blue-back .name-tab {
    position: absolute; right: 0; top: 112px; width: 300px; height: 40px;
    background: var(--blue); border-radius: 20px 0 0 20px;
    color: var(--white); font-size: 20px; line-height: 40px; text-align: center;
    font-family: "Open Sans", sans-serif; text-transform: uppercase;
  }
  .blue-back .contact-list {
    position: absolute; left: 40px; top: 190px;
    display: grid; grid-template-columns: 130px 30px auto; row-gap: 10px;
    font-size: 16px; color: var(--blue);
  }
  .blue-back .contact-label { font-weight: 700; color: var(--blue-deep); }
  .blue-back .bottom-stripe { position: absolute; left: 0; bottom: 0; width: 100%; height: 12px; background: linear-gradient(90deg, var(--blue-deep), var(--blue)); }

  /* ---------- Orange concept ---------- */
  .orange-front { background: var(--charcoal); }
  .orange-front .diagonal-band { position: absolute; inset: 0; background: var(--charcoal-deep); clip-path: polygon(58% 0, 82% 0, 62% 100%, 38% 100%); }
  .orange-front .brand-mark { position: absolute; left: 40px; top: 100px; font-size: 96px; color: var(--orange-logo); }
  .orange-front .brand-caption { position: absolute; left: 44px; top: 200px; color: var(--grey-text); }
  .orange-front .slogan { position: absolute; left: 44px; top: 226px; font-size: 20px; color: var(--white); letter-spacing: 5px; }

  .orange-back { background: var(--charcoal-deep); }
  .orange-back .accent-panel {
    position: absolute; inset: 0; background: var(--orange);
    clip-path: polygon(40% 0, 100% 0, 100% 100%, 40% 100%, 40% 24%, 33% 14%);
  }
  .orange-back .side-logo {
    position: absolute; left: 20px; top: 330px; width: 300px;
    transform: rotate(-90deg); transform-origin: 0 0;
  }
  .orange-back .side-logo .brand-mark { font-size: 64px; color: var(--orange-logo); }
  .orange-back .side-logo .brand-caption { display: block; color: var(--grey-text); font-size: 9px; margin-top: 6px; }
  .orange-back .card-name { position: absolute; left: 285px; top: 46px; font-family: "Michroma", sans-serif; font-size: 22px; color: var(--white); }
  .orange-back .contact-list {
    position: absolute; left: 285px; top: 110px;
    display: grid; grid-template-columns: 140px auto; row-gap: 8px;
    font-family: "Michroma", sans-serif; font-size: 13px; color: var(--white);
  }
  .orange-back .contact-email { grid-column: 1 / 3; margin-top: 10px; }

  /* ---------- Green concept ---------- */
  .green-front { background: var(--ink); }
  .green-front svg, .green-back svg { position: absolute; inset: 0; }
  .green-front .brand-mark { position: absolute; left: 130px; top: 92px; font-size: 84px; color: var(--green); }
  .green-front .brand-caption { position: absolute; left: 134px; top: 184px; color: var(--white); }
  .green-front .slogan { position: absolute; left: 134px; top: 206px; font-size: 18px; color: var(--white); }

  .green-back { background: var(--ink); }
  .green-back .brand-mark { position: absolute; right: 70px; top: 34px; font-size: 56px; color: var(--green); }
  .green-back .brand-caption { position: absolute; right: 112px; top: 94px; color: var(--white); font-size: 9px; }
  .green-back .card-name { position: absolute; left: 46px; top: 140px; font-family: "Playfair Display", serif; font-weight: 700; font-size: 26px; color: var(--white); }
  .green-back .contact-list { position: absolute; left: 46px; top: 190px; font-size: 14px; color: var(--white); line-height: 1.75; }
  .green-back .contact-email { margin-top: 10px; }
</style>
</head>
<body>

<section class="concept concept--blue">
  <div class="card card--front blue-front">
    <div class="brand-mark">FELLWAY</div>
    <div class="brand-caption">FELLWAY ELECTRICAL</div>
    <div class="slogan">Quality-Reliable-Service</div>
  </div>
  <div class="card card--back blue-back">
    <div class="top-band"></div>
    <div class="brand-mark">FELLWAY</div>
    <div class="brand-caption">FELLWAY ELECTRICAL</div>
    <div class="name-tab">Marcus Fell</div>
    <div class="contact-list">
      <span class="contact-label">Mobile</span><span>:</span><span>0491570156</span>
      <span class="contact-label">licence no#</span><span>:</span><span>vic 48107, nsw 315042k</span>
      <span class="contact-label">Email</span><span>:</span><span>marcusfell@tralvinet.com</span>
    </div>
    <div class="bottom-stripe"></div>
  </div>
</section>

<section class="concept concept--orange">
  <div class="card card--front orange-front">
    <div class="diagonal-band"></div>
    <div class="brand-mark">FELLWAY</div>
    <div class="brand-caption">FELLWAY ELECTRICAL</div>
    <div class="slogan">Quality-Reliable-Service</div>
  </div>
  <div class="card card--back orange-back">
    <div class="accent-panel"></div>
    <div class="side-logo">
      <span class="brand-mark">FELLWAY</span>
      <span class="brand-caption">FELLWAY ELECTRICAL</span>
    </div>
    <div class="card-name">Marcus fell</div>
    <div class="contact-list">
      <span>Mobile</span><span>: 0491570156</span>
      <span>licence no#</span><span>: vic 48107<br>&nbsp;&nbsp;nsw 315042k</span>
      <span class="contact-email">marcusfell@tralvinet.com</span>
    </div>
  </div>
</section>

<section class="concept concept--green">
  <div class="card card--front green-front">
    <svg width="620" height="354" viewBox="0 0 620 354" aria-hidden="true">
      <defs>
        <linearGradient id="green-wedge" x1="0" y1="0" x2="1" y2="1">
          <stop offset="0" stop-color="#8be64a"/>
          <stop offset="1" stop-color="#238f28"/>
        </linearGradient>
      </defs>
      <polygon points="0,0 150,0 0,260" fill="url(#green-wedge)"/>
      <polygon points="620,110 620,354 470,354" fill="url(#green-wedge)"/>
    </svg>
    <div class="brand-mark">FELLWAY</div>
    <div class="brand-caption">FELLWAY ELECTRICAL</div>
    <div class="slogan">Quality-Reliable-Service</div>
  </div>
  <div class="card card--back green-back">
    <svg width="620" height="354" viewBox="0 0 620 354" aria-hidden="true">
      <defs>
        <linearGradient id="green-corner" x1="0" y1="0" x2="1" y2="1">
          <stop offset="0" stop-color="#8be64a"/>
          <stop offset="1" stop-color="#238f28"/>
        </linearGradient>
      </defs>
      <polygon points="0,0 90,0 0,70" fill="url(#green-corner)"/>
      <polygon points="620,150 620,354 400,354" fill="url(#green-corner)"/>
    </svg>
    <div class="brand-mark">FELLWAY</div>
    <div class="brand-caption">FELLWAY ELECTRICAL</div>
    <div class="card-name">Marcus fell</div>
    <div class="contact-list">
      <div>Mobile : 0491570156</div>
      <div>licence no# : vic 48107, nsw 315042k</div>
      <div class="contact-email">marcusfell@tralvinet.com</div>
    </div>
  </div>
</section>

</body>
</html>
```